redesign existing business card

Re design our business cards. We want a modern elegant design, open to ideas front side must contain similar details in a fresh look and style, back side we are open to suggestions. MUST USE COMPANY COLORS, WE WANT BRANDING. Need more ideas see www.brightstoneyards.com - Project must be done in one of adobe products and all files and fonts must be submitted to us. THIS IS A MUST

Target Market(s)

home owners

Industry/Entity Type

Construction Company

Contact Information for Business Card

see existing card file for information

Font styles to use
Sans Serif

Colors
0455a3
3377b5
34a6d7
0592cd
85cae6
ffffff

Requirements
Must have
• company colors, logo, contact info this is all for front side. back side be creative.

```html
<!DOCTYPE html>
<html lang="en">
<head>
<meta charset="utf-8">
<title>Brightstone Yards – Business Card</title>
<link rel="stylesheet" href="https://fonts.googleapis.com/css2?family=Lato:wght@400;700&display=swap">
<style>
  :root {
    --stage: #2f2724;
    --card: #141414;
    --card-edge: #1d1d1d;
    --brand-deep: #0455a3;
    --brand-mid: #3377b5;
    --brand-sky: #34a6d7;
    --brand-bright: #0592cd;
    --brand-pale: #85cae6;
    --ink: #ffffff;
    --ink-soft: #e6e6e6;
    --divider: rgba(255, 255, 255, 0.08);
  }
  * { box-sizing: border-box; margin: 0; padding: 0; }
  html, body {
    width: 1200px;
    height: 844px;
    overflow: hidden;
    background: var(--stage);
    font-family: "Lato", sans-serif;
  }
  .stage {
    width: 1200px;
    height: 844px;
    display: flex;
    align-items: center;
    justify-content: center;
    gap: 60px;
  }
  .card {
    width: 525px;
    height: 300px;
    background: linear-gradient(160deg, var(--card-edge), var(--card) 60%);
    box-shadow: 0 18px 40px rgba(0, 0, 0, 0.55);
    position: relative;
    color: var(--ink);
  }

  /* Front */
  .card--front { display: flex; }
  .brand {
    width: 45%;
    display: flex;
    align-items: center;
    justify-content: center;
    gap: 10px;
    border-right: 1px solid var(--divider);
  }
  .brand__mark {
    width: 16px;
    height: 16px;
    background: var(--brand-bright);
  }
  .brand__name {
    font-weight: 700;
    font-size: 21px;
    color: var(--brand-mid);
  }
  .contact {
    width: 55%;
    padding: 52px 0 0 28px;
  }
  .contact__name {
    font-size: 21px;
    color: var(--brand-sky);
    margin-bottom: 12px;
  }
  .contact__address {
    font-size: 14px;
    line-height: 1.35;
    color: var(--ink-soft);
    margin-bottom: 14px;
  }
  .contact__list {
    list-style: none;
    font-size: 14px;
    line-height: 1.4;
    color: var(--ink-soft);
  }
  .contact__label {
    color: var(--brand-sky);
    display: inline-block;
    width: 16px;
  }

  /* Back */
  .card--back {
    display: flex;
    flex-direction: column;
    align-items: center;
    justify-content: center;
    text-align: center;
  }
  .services {
    list-style: none;
    font-size: 14px;
    line-height: 1.35;
    color: var(--ink-soft);
    margin-bottom: 20px;
  }
  .tagline {
    font-size: 14px;
    color: var(--brand-sky);
    margin-bottom: 22px;
  }
  .license {
    font-size: 11.5px;
    line-height: 1.4;
    color: var(--ink-soft);
  }
</style>
</head>
<body>
<main class="stage">
  <section class="card card--front" aria-label="Business card front">
    <div class="brand">
      <span class="brand__mark"></span>
      <span class="brand__name">Brightstone Yards</span>
    </div>
    <div class="contact">
      <h1 class="contact__name">Daniel Moreira</h1>
      <p class="contact__address">418 Harbor Ridge Ln suite 9<br>Coral Bay, FL 33410</p>
      <ul class="contact__list">
        <li><span class="contact__label">T:</span> (555) 310-2748</li>
        <li><span class="contact__label">T:</span> (555) 472-9063</li>
        <li><span class="contact__label">F:</span> (555) 218-6631</li>
        <li><span class="contact__label">E:</span> daniel@brightstoneyards.com</li>
        <li><span class="contact__label">W:</span>www.brightstoneyards.com</li>
      </ul>
    </div>
  </section>

  <section class="card card--back" aria-label="Business card back">
    <ul class="services">
      <li>Driveway Pool Renovation Custom</li>
      <li>Out-Doorkitchen</li>
      <li>Retaining Wall</li>
      <li>Paver Restoration</li>
      <li>H.O.A Project</li>
      <li>Patios &amp; Much More</li>
    </ul>
    <p class="tagline">Family Owned &amp; Operated</p>
    <p class="license">License &amp; Insured&nbsp; BRW 21 pv-40317-r PLM BCH u-5063<br>MARTIN MCPBT7810</p>
  </section>
</main>
</body>
</html>
```